Improving a camping website homepage header*

My client is very happy with his new website and its new functionalities. However, he's not very happy about the homepage design. Specifically, the header(this includes the menu, large header image and two columns beneath that). You can find the website here: http://lnkvo.example/siteTentra .

He forwarded me several other websites he likes. Which can be found in the attachments. I also included several pictures of the camping.

I'm looking for a design that will improve the header of the homepage with room for other global style chances. The logo cannot be changed.

Attachments
1) His old website homepage
2) Website mockup he liked.
3) Another website mockup he liked.

Other images can be found on the new website http://lnkvo.example/siteTentra or his old website http://lnkvo.example/formerSiteTentra.

Can you help us?
Updates

Hello guys. Here's a bit more information - Language used on the website is dutch. - The two columns left/right are supposed to link to Hire/Buy chalets. The client indicated that he finds these links important, but doesn't like the current design. I think this is partially the case because he doesn't like the icons. I'm looking forward to your designs!

Target Market(s)

30-50 year old wealthy people that want to purchase or rent cabins in the Netherlands.

Number of Pages Required

1 page

Colors

Designer to choose colors to be used in the design.

Requirements
Must have
• Improved header
Nice to have
• Global style changes
Should not have
• Logo changes

```html
<!DOCTYPE html>
<html lang="en">
<head>
<meta charset="utf-8">
<title>Parc Linderhof – Homepage</title>
<link href="https://fonts.googleapis.com/css2?family=Open+Sans:wght@400;600;700&family=Poiret+One&display=swap" rel="stylesheet">
<style>
:root{
  --backdrop:#3d3d3d;
  --green:#7a9a1a;
  --green-dark:#5f7a10;
  --ink:#1f1f1f;
  --grey:#6b6b6b;
  --dark:#222222;
  --white:#ffffff;
  --line:#cfcfcf;
}
*{margin:0;padding:0;box-sizing:border-box}
html,body{width:800px;height:1200px;overflow:hidden;background:var(--backdrop);font-family:"Open Sans",Arial,sans-serif;color:var(--ink)}
.page{position:absolute;left:170px;top:0;width:461px;height:1200px;background:var(--white);overflow:hidden}
.abs{position:absolute}
.btn{position:absolute;background:var(--green);color:var(--white);font-size:5px;font-weight:600;text-transform:uppercase;display:flex;align-items:center;justify-content:center;border-radius:2px}
.center{left:0;right:0;text-align:center}

/* nav */
.nav{left:0;top:0;width:461px;height:30px;background:var(--dark)}
.brand{left:20px;top:7px;display:flex;align-items:center;gap:4px;color:var(--green);font-size:8px;font-weight:600}
.brand .dot{width:14px;height:14px;border-radius:50%;background:var(--green)}
.menu{right:22px;top:9px;display:flex;gap:5px;font-size:6.4px;font-weight:700;color:var(--white)}
.menu span{padding:2px 2px}
.menu .active{background:var(--green);border-radius:2px}

/* hero */
.hero{left:0;top:30px;width:461px;height:170px;background:linear-gradient(180deg,#8fa7b3 0%,#4d6b3a 35%,#6f8a74 60%,#8c8a6a 80%,#3e4a2e 100%)}
.hero-title{top:78px;font-family:"Poiret One",sans-serif;font-size:27px;color:var(--white);letter-spacing:1px}
.hero-sub{top:124px;font-family:"Poiret One",sans-serif;font-size:11.5px;line-height:16px;color:var(--white)}
.dots{display:flex;gap:2px;justify-content:center}
.dots i{width:4px;height:4px;border-radius:50%;border:1px solid var(--white)}
.dots i:first-child{background:var(--white)}

/* intro */
.intro-title{left:20px;top:228px;font-size:8.2px;font-weight:600;letter-spacing:.3px}
.intro-rule{left:20px;top:240px;width:40px;height:1.5px;background:var(--green)}
.intro-text{left:20px;top:251px;width:275px;font-size:7.2px;line-height:11px;color:var(--grey)}
.intro-text p{margin-bottom:12px}
.alert{left:311px;top:225px;width:62px;height:109px;background:var(--dark);border-radius:3px 0 0 3px;color:var(--white);text-align:center;padding-top:5px}
.alert .bang{width:17px;height:17px;margin:0 auto 3px;border-radius:50%;background:var(--green);font-size:10px;font-weight:700;line-height:17px}
.alert .head{font-size:7.4px;line-height:11px}
.alert .small{font-size:4.8px;line-height:7.6px;margin-top:2px}
.info{left:373px;top:225px;width:65px;height:109px;background:var(--green);border-radius:0 3px 3px 0;color:var(--white);padding:7px 8px;font-size:4.8px;line-height:7.5px}
.info hr{border:0;border-top:1px solid var(--white);margin:5px 0 11px}

/* booking band */
.band{left:0;top:362px;width:461px;height:92px;background:linear-gradient(180deg,#3d4a2a,#5a6b3c 50%,#3e4b2c)}
.band-title{top:380px;font-size:10.5px;font-weight:700;color:var(--white)}
.band-sub{top:395px;font-size:7.4px;color:var(--white)}

/* villa */
.villa-photo{left:20px;top:482px;width:130px;height:105px;border:1px solid #444;background:linear-gradient(180deg,#a8b8c8 0%,#dcdcd6 40%,#6e8a4a 75%,#4a5a34 100%)}
.villa-title{left:162px;top:482px;font-size:10.5px;font-weight:700}
.villa-rule{left:162px;top:496px;width:30px;height:1.5px;background:var(--green)}
.villa-text{left:162px;top:507px;width:276px;font-size:4.8px;line-height:7.4px}
.villa-text em{color:var(--green);font-style:normal}
.features{left:162px;top:536px;width:276px;display:grid;grid-template-columns:repeat(3,87px);column-gap:7px}
.features div{font-size:4.8px;height:16.5px;padding-top:3px;border-bottom:1px solid #444;display:flex;gap:4px}
.features b{color:var(--green);font-weight:700}

/* related */
.related{left:0;top:623px;width:461px;height:183px;background:linear-gradient(180deg,#5a4a3c 0%,#6c5a48 35%,#4a4a44 70%,#3c3c38 100%)}
.related-rule{left:19px;top:658px;width:420px;height:1px;background:#bbb}
.related-title{top:675px;font-size:10.5px;font-weight:700;color:var(--white)}
.work{top:697px;width:101px;height:89px;border:1px solid var(--white);background:linear-gradient(180deg,#9fb0b8 0%,#c8ccc4 40%,#5d7a3a 75%,#3e5228 100%)}
.work .lbl{position:absolute;left:6px;bottom:20px;color:var(--white);font-size:6.3px;font-weight:700}
.work .price{position:absolute;left:7px;bottom:6px;background:var(--green);color:var(--white);font-size:3.8px;padding:2px 3px;border-radius:1px}

/* offers */
.offers-title{top:826px;font-size:10.5px;font-weight:700}
.rule-c{left:220px;width:22px;height:1.5px;background:var(--green)}
.offer-photo{left:21px;top:861px;width:210px;height:115px;border:2px solid #222;background:linear-gradient(180deg,#a9b9c9 0%,#e0e0dc 38%,#7e9458 72%,#4d6030 100%)}
.offer-head{left:247px;top:857px;font-size:10.5px;font-weight:700}
.offer-list{left:247px;top:875px;width:183px;list-style:none}
.offer-list li{height:15px;display:flex;align-items:center;justify-content:space-between;font-size:4.9px}
.offer-list li span::before{content:"•";margin-right:5px}
.offer-list b{background:var(--green);color:var(--white);font-size:4.7px;width:51px;text-align:center;padding:1.5px 0;border-radius:1.5px}
.special-title{top:992px;font-size:10.5px;font-weight:700}
.special-text{top:1013px;left:50px;right:50px;text-align:center;font-size:4.9px;line-height:7.3px}

/* signup */
.signup{left:0;top:1072px;width:461px;height:58px;background:var(--green);color:var(--white)}
.signup .pre{left:20px;top:24px;font-size:4.8px}
.signup .big{left:19px;top:31px;font-size:7.4px;font-weight:700}
.field{top:27px;width:105px;font-size:4.6px;padding-bottom:4px;border-bottom:1px solid rgba(255,255,255,.7)}
.signup .go{left:378px;top:30px;font-size:4.8px;font-weight:600}

/* footer */
.footer{left:0;top:1130px;width:461px;height:70px;background:var(--dark);color:var(--white)}
.f-brand{left:22px;top:18px;display:flex;align-items:center;gap:4px;color:var(--green);font-size:7.4px;font-weight:600}
.f-brand .dot{width:12px;height:12px;border-radius:50%;background:var(--green)}
.f-about{left:103px;top:27px;width:78px;font-size:4.8px;line-height:7.2px}
.f-about2{left:25px;top:51px;width:160px;font-size:4.8px;line-height:7.2px}
.f-col{top:18px;font-size:4.8px;line-height:6.6px}
.f-col strong{display:block;font-weight:700;margin-top:3px}
.social{display:flex;gap:2px;margin-top:2px}
.social i{width:6px;height:6px;border-radius:50%;background:var(--white)}
</style>
</head>
<body>
<div class="page">

  <header class="abs nav">
    <div class="abs brand"><span class="dot"></span>Parc Linderhof</div>
    <nav class="abs menu">
      <span>HOME</span><span class="active">ABOUT</span><span>CONTACT</span><span>LOCATION</span><span>QUOTE</span><span>GALLERY</span><span>REVIEWS</span>
    </nav>
  </header>

  <section class="abs hero" role="img" aria-label="Aerial photo of the park lake with beach, parasols and chalets among trees"></section>
  <h1 class="abs center hero-title">LOREM IPSUM</h1>
  <p class="abs center hero-sub">dolor sit amet, consectetur adipiscing elit.<br>Integer nec odio. Praesent libero.</p>
  <div class="abs center dots" style="top:186px"><i></i><i></i><i></i></div>

  <h2 class="abs intro-title">PARC LINDERHOF IS A SPECTACULAR LUXURY</h2>
  <div class="abs intro-rule"></div>
  <div class="abs intro-text">
    <p>dolor sit amet, consectetur adipiscing elit. Integer nec odio.</p>
    <p>Praesent libero. Sed cursus ante dapibus diam. Sed nisi. Nulla quis sem at nibh elementum imperdiet. Duis sagittis ipsum. Praesent mauris.</p>
  </div>
  <div class="btn" style="left:21px;top:309px;width:44px;height:14px">Learn more</div>

  <div class="abs alert">
    <div class="bang">!</div>
    <div class="head">Oops! er is<br>iets<br>misgaan</div>
    <div class="small">dolor sit amet,<br>consectetur<br>adipiscing elit.<br>Integer nec odio.<br>Praesent libero.<br>Sed</div>
  </div>
  <div class="abs info">
    <svg width="6" height="8" viewBox="0 0 12 16"><path d="M6 0a6 6 0 0 0-6 6c0 4.5 6 10 6 10s6-5.5 6-10a6 6 0 0 0-6-6zm0 8.5A2.5 2.5 0 1 1 6 3.5a2.5 2.5 0 0 1 0 5z" fill="#fff"/></svg>
    <div>address<br>dolor sit amet, c<br>onsectetur adipis<br>cing elit. Intege<br>r nec odio. Praes</div>
    <hr>
    <svg width="7" height="7" viewBox="0 0 16 16"><path d="M3.6 1l2.6 3-1.5 2a9 9 0 0 0 5 5l2-1.5 3 2.6-1.7 2.4C6.8 15 1 9.2 1.2 2.7z" fill="#fff"/></svg>
    <div>call us<br>0355 210 448</div>
  </div>

  <section class="abs band" role="img" aria-label="Photo of a green pond edge with reeds"></section>
  <h2 class="abs center band-title">ENJOY THE BESTOF PORTO</h2>
  <p class="abs center band-sub">Make your reservation right now with the bestprice</p>
  <div class="btn" style="left:210px;top:423px;width:43px;height:15px">Book now</div>

  <div class="abs villa-photo" role="img" aria-label="Photo of a white wooden chalet with terrace and garden"></div>
  <div class="abs dots" style="left:115px;top:577px"><i></i><i></i><i></i></div>
  <h2 class="abs villa-title">VILLA MONACOOVERVIEW</h2>
  <div class="abs villa-rule"></div>
  <p class="abs villa-text">dolor sit amet, consectetur adipiscing elit. Integer nec odio. Praesent libero. Sed cursus ante dapibus diam. Sed nisi.dolor sit amet, consectetur adipiscing elit. Integer nec odio. <em>( VIEW MORE )</em></p>
  <div class="abs features">
    <div><b>✓</b>dolor sit amet, consectetur</div><div><b>✓</b>dolor sit amet, consectetur</div><div><b>✓</b>dolor sit amet, consectetur</div>
    <div><b>✓</b>dolor sit amet</div><div><b>✓</b>dolor sit amet</div><div><b>✓</b>dolor sit amet</div>
    <div style="border:0"><b>✓</b>dolor sit amet, consectetur</div><div style="border:0"><b>✓</b>dolor sit amet, consectetur</div><div style="border:0"><b>✓</b>dolor sit amet, consectetur</div>
  </div>

  <section class="abs related" role="img" aria-label="Darkened photo of wooden log cabins"></section>
  <div class="abs related-rule"></div>
  <h2 class="abs center related-title">RELATED WORK</h2>
  <div class="abs work" style="left:19px" role="img" aria-label="Photo of a mobile home on a green plot"><span class="lbl">KAVEL 49</span><span class="price">$94.500</span></div>
  <div class="abs work" style="left:126px" role="img" aria-label="Photo of a white chalet with terrace"><span class="lbl">KAVEL 49</span><span class="price">$94.500</span></div>
  <div class="abs work" style="left:233px" role="img" aria-label="Photo of a mobile home on a green plot"><span class="lbl">KAVEL 49</span><span class="price">$94.500</span></div>
  <div class="abs work" style="left:339px" role="img" aria-label="Photo of a white chalet with terrace"><span class="lbl">KAVEL 49</span><span class="price">$94.500</span></div>

  <h2 class="abs center offers-title">SPECIAL OFFERS</h2>
  <div class="abs rule-c" style="top:842px"></div>
  <div class="abs offer-photo" role="img" aria-label="Photo of a white chalet with garden furniture on the terrace"></div>
  <h3 class="abs offer-head">OFFERS</h3>
  <ul class="abs offer-list">
    <li><span>dolor sit amet, consectetur adipiscing elit.</span><b>$1248.900</b></li>
    <li><span>dolor sit amet, consectetur adipiscing elit.</span><b>$1248.900</b></li>
    <li><span>dolor sit amet, consectetur adipiscing elit.</span><b>$1248.900</b></li>
    <li><span>dolor sit amet, consectetur adipiscing elit.</span><b>$1248.900</b></li>
    <li><span>dolor sit amet, consectetur adipiscing elit.</span><b>$1248.900</b></li>
    <li><span>dolor sit amet, consectetur adipiscing elit.</span><b>$1248.900</b></li>
    <li><span>dolor sit amet, consectetur adipiscing elit.</span><b>$1248.900</b></li>
  </ul>
  <h2 class="abs center special-title">PORTO SPECIAL</h2>
  <div class="abs rule-c" style="top:1007px"></div>
  <p class="abs special-text">dolor sit amet, consectetur adipiscing elit. Integer nec odio. Praesent libero. Sed cursus ante dapibus diam. Sed nisi. Nulla quis sem at nibh elementum imperdiet. Duis sagittis ipsum. Praesent mauris. Fusce nec tellus sed augue semper porta. Mauris massa.</p>
  <div class="btn" style="left:214px;top:1041px;width:33px;height:14px">View all</div>

  <section class="abs signup">
    <div class="abs pre">SIGN UP NOW FOR</div>
    <div class="abs big">EXCLUSIVE SPECIAL OFFERS:</div>
    <div class="abs field" style="left:139px">FULL NAME*</div>
    <div class="abs field" style="left:250px">EMAIL ADDRESS*</div>
    <div class="abs go">SUBSCRIBE NOW</div>
  </section>

  <footer class="abs footer">
    <div class="abs f-brand"><span class="dot"></span>Parc Linderhof</div>
    <p class="abs f-about">dolor sit amet, consecteturDR adipiscing elit. Integer nec odi</p>
    <p class="abs f-about2">Praesent libero. Sed cursus ante dapibus diam. Sed nisi. Nulla quis sem at nibh elementum imperdiet. Duis sagittis ipsum. Duis sagi</p>
    <div class="abs f-col" style="left:201px">
      <svg width="6" height="8" viewBox="0 0 12 16"><path d="M6 0a6 6 0 0 0-6 6c0 4.5 6 10 6 10s6-5.5 6-10a6 6 0 0 0-6-6zm0 8.5A2.5 2.5 0 1 1 6 3.5a2.5 2.5 0 0 1 0 5z" fill="#fff"/></svg>
      <strong>ADDRESS</strong>LOREM IPSUM DODO JI<br>MUN NUM LO LOREP SUM SUD
    </div>
    <div class="abs f-col" style="left:313px">
      <svg width="8" height="8" viewBox="0 0 16 16"><path d="M3.6 1l2.6 3-1.5 2a9 9 0 0 0 5 5l2-1.5 3 2.6-1.7 2.4C6.8 15 1 9.2 1.2 2.7z" fill="#fff"/></svg>
      <strong>CALL US</strong>(003) 055 210 4480
    </div>
    <div class="abs f-col" style="left:406px">
      <svg width="8" height="8" viewBox="0 0 16 16"><circle cx="12" cy="3" r="2.2" fill="#fff"/><circle cx="4" cy="8" r="2.2" fill="#fff"/><circle cx="12" cy="13" r="2.2" fill="#fff"/><path d="M12 3L4 8l8 5" stroke="#fff" stroke-width="1.3" fill="none"/></svg>
      <strong>FOLLOW US</strong>
      <div class="social"><i></i><i></i><i></i><i></i></div>
    </div>
  </footer>

</div>
</body>
</html>
```